Dining hall menu app needs a redesign

We are looking for a redesign of our app TrayPlate which is available for iOS for free on the Kestrel AppHub.

The app allows students of most of Germany's universities to show the menu of their university's dining hall. Currently there are about 400 dining halls to view the menu of. A menu contains the a list of meals for the next couple of days (usually for the next 5-7 days). Each meal can be rated by the users and photos can be uploaded. The following data should be visible for each meal in the meal list:
- The date the meal is available
- The meal category (usually a short text, categorizing the meal)
- Name of the meal (can be very long but it's ok to truncate it after the second line)
- Average meal rating (5-star rating)
- A photo of the meal
- Up to 4 prices (e.g. usually students pay less than employees, which is why multiple prices for the same meal are available. In the menu list only the prices are shown)

When selecting a meal, more details about the meal are shown:
- Full meal name
- Up to 4 prices including the price type (e.g. Student: 3.40€, Employees: 4.20€)
- Total number of ratings
- Total number of comments
- A list of additives and info-texts about the meal (e.g. whether the meal is vegetarian, or contains food additives)
- A list of photos including a relative date when the photo has been taken (e.g. "2 months ago")

Additionally a user should be able to add a review to the meal (5 star rating and an optional comment), view the list of comments, take a photo of the meal and to share it on chatterbook/blipster/via email.

All views show an advertisement banner on the bottom of the view.

The design should be very modern and clean. We don't like a skeuomorphic design. The content of the app is most important. Other than that you are free to design something pretty.
Updates

Target Market(s)

Students (age between 19 and 30)

Industry/Entity Type

University

Requirements
Must have
• At least we need a redesign of the meal list, the meal detail page, the app-logo and the splashscreen.
Nice to have
• Design for the meal review page, the dining hall list and the favorites list.
Should not have
• No skeuomorphic design and not too many colors.

```html
<!DOCTYPE html>
<html lang="en">
<head>
<meta charset="utf-8">
<title>TrayPlate – State</title>
<link rel="stylesheet" href="https://fonts.googleapis.com/css2?family=Arimo:wght@400;700&family=Source+Sans+3:wght@400;600;700&display=swap">
<style>
  :root {
    --status-bg: #000000;
    --status-text: #ffffff;
    --nav-top: #a30e0e;
    --nav-bottom: #7d0303;
    --nav-edge: #4d0000;
    --list-bg: #ededed;
    --row-line: #cfcfcf;
    --row-highlight: #f7f7f7;
    --row-text: #5f5f5f;
    --ad-bg-a: #6f8a3c;
    --ad-bg-b: #9a7b4b;
    --ad-bg-c: #3d5c7a;
    --cta-red: #c8101a;
    --cta-edge: #ffffff;
    --tab-bg: #3f0000;
    --tab-top: #5a0202;
    --tab-muted: #8e0c0c;
    --tab-active: #980808;
    --tab-active-edge: #b41616;
    --white: #ffffff;
  }
  * { box-sizing: border-box; margin: 0; padding: 0; }
  html, body { width: 800px; height: 1200px; overflow: hidden; background: var(--list-bg); }
  .screen { position: relative; width: 800px; height: 1200px; overflow: hidden; font-family: "Source Sans 3", sans-serif; }

  .status-bar { position: absolute; top: 0; left: 0; width: 800px; height: 50px; background: var(--status-bg); color: var(--status-text); font-family: "Arimo", sans-serif; font-weight: 700; font-size: 28px; }
  .status-carrier { position: absolute; left: 10px; top: 9px; font-weight: 400; }
  .status-wifi { position: absolute; left: 140px; top: 12px; }
  .status-time { position: absolute; left: 0; right: 0; top: 9px; text-align: center; }
  .status-location { position: absolute; left: 688px; top: 13px; }
  .status-battery { position: absolute; left: 738px; top: 14px; }

  .nav-bar { position: absolute; top: 50px; left: 0; width: 800px; height: 112px; background: linear-gradient(var(--nav-top), var(--nav-bottom)); border-bottom: 3px solid var(--nav-edge); }
  .nav-title { position: absolute; left: 0; right: 0; top: 22px; text-align: center; color: var(--white); font-weight: 700; font-size: 48px; letter-spacing: 0.5px; }
  .refresh-button { position: absolute; left: 704px; top: 20px; width: 84px; height: 68px; border-radius: 8px; background: linear-gradient(#b01616, #8c0606); border: 2px solid #c42a2a; display: flex; align-items: center; justify-content: center; }

  .state-list { position: absolute; top: 162px; left: 0; width: 800px; list-style: none; }
  .state-row { height: 110px; line-height: 108px; padding-left: 64px; font-size: 40px; color: var(--row-text); border-bottom: 2px solid var(--row-line); box-shadow: inset 0 2px 0 var(--row-highlight); }

  .ad-banner { position: absolute; top: 952px; left: 0; width: 800px; height: 123px; }
  .ad-artwork { position: absolute; inset: 0; background: linear-gradient(100deg, var(--ad-bg-c) 0%, var(--ad-bg-b) 25%, var(--ad-bg-a) 55%, var(--ad-bg-b) 80%, #5b4a3a 100%); }
  .ad-brand { position: absolute; left: 34px; top: 14px; padding: 4px 8px; background: var(--white); color: #2a6cb0; font-weight: 700; font-size: 18px; }
  .ad-info { position: absolute; left: 10px; top: 88px; width: 28px; height: 28px; border-radius: 50%; border: 2px solid #dddddd; color: #dddddd; font-size: 18px; text-align: center; line-height: 24px; font-family: "Arimo", sans-serif; }
  .ad-cta { position: absolute; left: 566px; top: 20px; width: 196px; height: 88px; border-radius: 6px; background: linear-gradient(#e01a22, #a8070e); border: 3px solid var(--cta-edge); color: var(--white); font-weight: 700; font-size: 44px; text-align: center; line-height: 80px; }

  .tab-bar { position: absolute; top: 1075px; left: 0; width: 800px; height: 125px; background: linear-gradient(var(--tab-top), var(--tab-bg)); }
  .tab { position: absolute; top: 0; height: 125px; text-align: center; color: var(--tab-muted); font-weight: 700; font-size: 29px; }
  .tab-map { left: 60px; width: 120px; }
  .tab-favorites { left: 600px; width: 160px; }
  .tab-icon { display: block; margin: 14px auto 4px; }
  .tab-canteens { position: absolute; left: 236px; top: 1038px; width: 328px; height: 328px; border-radius: 50%; background: radial-gradient(circle at 50% 30%, #a80c0c, var(--tab-active) 60%, #7c0404); border: 3px solid var(--tab-active-edge); }
  .tab-canteens-icon { position: absolute; left: 114px; top: 20px; }
  .tab-canteens-label { position: absolute; left: 0; right: 0; top: 100px; text-align: center; color: var(--white); font-weight: 700; font-size: 33px; }
</style>
</head>
<body>
<div class="screen">

  <header class="status-bar">
    <span class="status-carrier">Carrier</span>
    <svg class="status-wifi" width="32" height="24" viewBox="0 0 32 24" aria-hidden="true">
      <path d="M16 22 L11 16 A8 8 0 0 1 21 16 Z" fill="#fff"/>
      <path d="M6 11 A14 14 0 0 1 26 11" stroke="#fff" stroke-width="4" fill="none"/>
      <path d="M1 6 A21 21 0 0 1 31 6" stroke="#fff" stroke-width="4" fill="none"/>
    </svg>
    <span class="status-time">1:12 AM</span>
    <svg class="status-location" width="26" height="26" viewBox="0 0 26 26" aria-hidden="true">
      <path d="M24 2 L2 12 L13 13 L14 24 Z" fill="#fff"/>
    </svg>
    <svg class="status-battery" width="52" height="24" viewBox="0 0 52 24" aria-hidden="true">
      <rect x="1" y="1" width="44" height="22" rx="3" fill="none" stroke="#fff" stroke-width="2"/>
      <rect x="4" y="4" width="38" height="16" fill="#fff"/>
      <rect x="46" y="8" width="4" height="8" fill="#fff"/>
    </svg>
  </header>

  <nav class="nav-bar">
    <h1 class="nav-title">State</h1>
    <div class="refresh-button" role="button" aria-label="Refresh">
      <svg width="44" height="44" viewBox="0 0 44 44" aria-hidden="true">
        <path d="M34 14 A15 15 0 1 0 36 28" fill="none" stroke="#fff" stroke-width="7" stroke-linecap="round"/>
        <path d="M26 6 L40 6 L38 20 Z" fill="#fff"/>
      </svg>
    </div>
  </nav>

  <ul class="state-list">
    <li class="state-row">Baden-Württemberg</li>
    <li class="state-row">Bayern</li>
    <li class="state-row">Berlin</li>
    <li class="state-row">Brandenburg</li>
    <li class="state-row">Hamburg</li>
    <li class="state-row">Hessen</li>
    <li class="state-row">Niedersachsen</li>
    <li class="state-row">Nordrhein-Westfalen</li>
  </ul>

  <aside class="ad-banner">
    <div class="ad-artwork" role="img" aria-label="Game advertisement artwork showing a village scene"></div>
    <span class="ad-brand">Gladewood</span>
    <span class="ad-info">i</span>
    <span class="ad-cta">Spielen</span>
  </aside>

  <footer class="tab-bar">
    <div class="tab tab-map">
      <svg class="tab-icon" width="50" height="60" viewBox="0 0 50 60" aria-hidden="true">
        <path d="M25 58 L10 38 A20 20 0 1 1 40 38 Z" fill="none" stroke="#8e0c0c" stroke-width="4"/>
        <path d="M25 14 V32 M16 23 H34" stroke="#8e0c0c" stroke-width="4"/>
      </svg>
      Map
    </div>
    <div class="tab tab-favorites">
      <svg class="tab-icon" width="60" height="58" viewBox="0 0 60 58" aria-hidden="true">
        <path d="M30 2 L37 21 L58 21 L41 34 L47 55 L30 42 L13 55 L19 34 L2 21 L23 21 Z" fill="#8e0c0c"/>
      </svg>
      Favorites
    </div>
  </footer>

  <div class="tab-canteens">
    <svg class="tab-canteens-icon" width="100" height="80" viewBox="0 0 100 80" aria-hidden="true">
      <g fill="#b81a1a" opacity="0.8">
        <rect x="16" y="0" width="4" height="26"/>
        <rect x="24" y="0" width="4" height="26"/>
        <rect x="32" y="0" width="4" height="26"/>
        <path d="M14 24 H38 L30 38 V80 H22 V38 Z"/>
        <path d="M70 0 C86 10 84 40 76 44 V80 H68 Z"/>
      </g>
    </svg>
    <span class="tab-canteens-label">Canteens</span>
  </div>

</div>
</body>
</html>
```